Law Firm Needs a new Website Design

We need a new website design for our law firm located in Manhattan (Law Offices of Desmond T. Halvorsen, PLLC).
We have an existing logo that we will to continue using, which can be found in www.HalvorsenLegal.example.
The Peak Counsel, Premier Barristers Logo should also be reflected near the bottom of the Home page.
The website will be 6 pages.

Deliverables:
I want a
1) home page,
2) About Us/Practice Areas page,
3) attorneys,
4) News and Articles page, and
5) Contact and Directions/Privacy Policy page.

The colors of my logo should be in the website.
I also like a touch of black and red.

The website should project "excellence."
We seek to provide the highest quality legal services.
We handle estate planning, wills, trusts, planning for people with disabilities, asset protection and preservation, Medicaid planning, hospital safe discharge, nursing home placement, powers of attorney, health care proxies, living wills, guardianships, probate, estate administration and related litigation.

I would like the colors of my Logo used (including shading where appropriate).
I also want some black on the borders and/or bottom and some red touches throughout the page.

My Logo should appear everywhere that "Law Offices Of Desmond T. Halvorsen, PLLC" appears.
I want the badges for Peak counsel, Premier Barristers, Premier Legal Practices, and ZENLO on the Home page.
I do not want too much text on the home page.

We would also like the website to have coding.
The final design should also communicate quality, expertise and stability.
Great start so far by the people who submitted designs.
Thank you.

3276b5
ec1f27
474747

• Please use my logo each time you mention Law Offices of Desmond T. Halvorsen, PLLC. Please include the Peakcounsel, Premier Barristers, Premier Legal Practices and Zenlo rating Badges on the web home page. I only wish to be contacted by phone. I am not including testimonials and am only using the New York City address.
• Prefer illustrations to photos regarding practice areas
• Testimonials, contact me by email, free consultation.

```html
<!DOCTYPE html>
<html lang="en">
<head>
<meta charset="utf-8">
<title>Law Offices of Desmond T. Halvorsen, PLLC</title>
<link href="https://fonts.googleapis.com/css2?family=Cinzel:wght@400;700&family=Lato:wght@400;700&display=swap" rel="stylesheet">
<style>
:root{
  --brand-blue:#3276b5;
  --panel-blue:#3c86c6;
  --deep-blue:#1f4f86;
  --link-blue:#4aa0e6;
  --brand-red:#ec1f27;
  --charcoal:#474747;
  --ink:#1a1a1a;
  --footer:#2b2b2b;
  --black:#000;
  --white:#fff;
  --soft-grey:#e9e9e9;
}
*{box-sizing:border-box;margin:0;padding:0}
html,body{width:1200px;height:2995px;overflow:hidden}
body{position:relative;background:var(--white);font-family:'Lato',Arial,sans-serif;color:var(--ink)}
.abs{position:absolute}

/* header */
.site-header{left:0;top:0;width:1200px;height:112px;background:linear-gradient(#fff,#f3f5f8)}
.brand-name{left:56px;top:26px;display:flex;align-items:center;gap:14px}
.brand-square{width:50px;height:50px;background:var(--brand-blue)}
.brand-text{font-family:'Cinzel',serif;font-size:30px;color:var(--deep-blue);line-height:1.05;width:540px}
.phone-pill{right:0;top:0;width:170px;height:34px;background:var(--brand-blue);border-radius:0 0 0 18px;color:#fff;font-weight:700;font-size:18px;display:flex;align-items:center;justify-content:center;gap:8px}
.social{right:26px;top:58px;display:flex;gap:10px}
.social span{width:32px;height:32px;border-radius:4px}
.top-rule{left:0;top:0;width:1030px;height:3px;background:var(--brand-blue)}

.main-nav{left:52px;top:112px;width:1098px;height:38px;background:linear-gradient(#4c8fcf,#1f5a9b);display:flex;border-radius:3px 3px 0 0}
.main-nav a{color:#fff;text-decoration:none;font-size:15px;display:flex;align-items:center;justify-content:center;border-right:1px solid rgba(255,255,255,.35)}
.main-nav a.active{background:var(--brand-red)}
.main-nav a:last-child{border-right:none}

/* hero */
.hero{left:0;top:150px;width:1200px;height:515px;background:linear-gradient(180deg,#9fb2c6 0%,#6f7f8f 40%,#3f4a55 100%)}
.hero-title{left:0;top:370px;width:1200px;text-align:center;font-family:'Cinzel',serif;color:#fff;font-size:40px;line-height:1.1}
.hero-title small{display:block;font-size:22px}
.slide-arrow{top:382px;width:44px;height:44px;background:rgba(255,255,255,.85)}
.slide-arrow.left{left:0;border-radius:0 6px 6px 0}
.slide-arrow.right{right:0;border-radius:6px 0 0 6px}

/* welcome */
.welcome{left:0;top:665px;width:1200px;height:385px;background:#fff}
.welcome-line{left:0;top:705px;width:1200px;display:flex;justify-content:center;align-items:center;gap:22px}
.welcome-line .lead{font-size:28px;color:var(--ink)}
.welcome-line .name{font-family:'Cinzel',serif;font-size:26px;color:var(--deep-blue)}
.dotted{left:246px;top:786px;width:710px;border-top:2px dotted #b9b9b9}
.excellence{left:0;top:812px;width:1200px;text-align:center;font-family:'Cinzel',serif;font-size:30px;color:var(--brand-red);letter-spacing:1px}
.intro{left:80px;top:864px;width:1040px;text-align:center;font-size:16px;line-height:27px;color:var(--ink)}
.read-more{left:538px;top:966px;width:118px;height:32px;background:var(--brand-red);color:#fff;font-size:15px;display:flex;align-items:center;justify-content:flex-end;padding-right:10px;border-radius:2px}
.read-more i{position:absolute;left:-4px;top:2px;width:28px;height:28px;background:var(--brand-blue);border:2px solid #fff;transform:rotate(45deg)}

/* practice areas */
.practice-left{left:0;top:1050px;width:598px;height:1135px;background:var(--panel-blue)}
.practice-right{left:598px;top:1050px;width:602px;height:1135px;background:var(--black)}
.practice-tab{left:400px;top:1046px;width:400px;height:60px}
.practice-heading{left:400px;top:1058px;width:400px;text-align:center;font-family:'Cinzel',serif;font-size:28px;color:var(--ink)}
.practice-heading span{color:var(--brand-blue)}
.area{width:480px}
.area h3{font-size:19px;font-weight:400;margin-bottom:6px}
.area p{font-size:13px;line-height:20px;color:#fff;font-weight:700}
.area.on-blue h3{color:#fff}
.area.on-black h3{color:var(--link-blue)}
.diamond{width:120px;height:120px}

/* tagline */
.tagline-band{left:0;top:2185px;width:1200px;height:350px;background:linear-gradient(#c9c9c9,#f4f4f4 30%,#f4f4f4 70%,#d6d6d6)}
.tagline{left:0;top:2232px;width:1200px;text-align:center;font-family:'Cinzel',serif;font-size:36px;line-height:44px;color:var(--ink);letter-spacing:1px}
.accreditations{left:78px;top:2356px;width:1044px;height:144px;background:linear-gradient(#4a8cc8,#2e6aa8);border-radius:4px}
.accred-label{left:104px;top:2390px;color:#fff;font-size:27px;line-height:34px}
.partner{color:#fff;font-size:30px;top:2410px}

/* call band */
.call-band{left:0;top:2535px;width:1200px;height:135px;background:linear-gradient(#2e64a0,#4a86c4)}
.call-text{left:374px;top:2590px;color:#fff;font-size:24px;letter-spacing:1px}
.call-phone{left:682px;top:2578px;color:#fff;font-size:34px;font-weight:700}

/* footer */
.site-footer{left:0;top:2670px;width:1200px;height:270px;background:var(--footer)}
.foot-title{color:#fff;font-size:19px;top:2696px;padding-bottom:8px;border-bottom:1px dotted #777;width:155px}
.quick-links{left:78px;top:2742px;list-style:none}
.quick-links li{color:#fff;font-size:13px;line-height:27.5px}
.quick-links li::before{content:'›';margin-right:10px;font-weight:700}
.contact-row{left:358px;color:#fff;font-size:13px;line-height:18px;display:flex;gap:12px}
.contact-row svg{flex:none}
.map-area{left:610px;top:2750px;width:275px;height:145px;background:linear-gradient(135deg,#ece7dc,#d9dde2)}
.copyright-bar{left:0;top:2940px;width:1200px;height:55px;background:#111;color:#fff;font-size:13px;display:flex;align-items:center;justify-content:center}
</style>
</head>
<body>

<header class="site-header abs"></header>
<div class="top-rule abs"></div>
<div class="brand-name abs"><span class="brand-square"></span><span class="brand-text">Law Offices of Desmond T. Halvorsen, PLLC</span></div>
<div class="phone-pill abs">
  <svg width="14" height="14" viewBox="0 0 24 24"><path fill="#fff" d="M6.6 10.8a15 15 0 0 0 6.6 6.6l2.2-2.2c.3-.3.7-.4 1-.2 1.1.4 2.3.6 3.6.6.6 0 1 .4 1 1V20c0 .6-.4 1-1 1A17 17 0 0 1 3 4c0-.6.4-1 1-1h3.5c.6 0 1 .4 1 1 0 1.3.2 2.5.6 3.6.1.3 0 .7-.2 1z"/></svg>
  (212) 555-0148
</div>
<div class="social abs">
  <span style="background:#3b5998"></span><span style="background:#2fa7e0"></span><span style="background:#d94a38"></span><span style="background:#1c84c6"></span>
</div>

<nav class="main-nav abs">
  <a class="active" href="#" style="width:80px">Home</a>
  <a href="#" style="width:170px">Practice Areas</a>
  <a href="#" style="width:184px">Privacy Policy</a>
  <a href="#" style="width:180px">Attorneys</a>
  <a href="#" style="width:268px">Contact &amp; Directions</a>
  <a href="#" style="width:216px">News</a>
</nav>

<section class="hero abs" role="img" aria-label="Aerial photograph of the Manhattan skyline with skyscrapers and the river beyond"></section>
<div class="hero-title abs"><small>Law Offices of</small>Desmond T. Halvorsen<small>PLLC</small></div>
<div class="slide-arrow left abs"><svg width="44" height="44" viewBox="0 0 44 44"><path d="M26 12 16 22l10 10" fill="none" stroke="#1f4f86" stroke-width="4"/></svg></div>
<div class="slide-arrow right abs"><svg width="44" height="44" viewBox="0 0 44 44"><path d="M18 12l10 10-10 10" fill="none" stroke="#1f4f86" stroke-width="4"/></svg></div>

<section class="welcome abs"></section>
<div class="welcome-line abs"><span class="lead">Welcome to</span><span class="name">Law Offices of Desmond T. Halvorsen, PLLC</span></div>
<div class="dotted abs"></div>
<h2 class="excellence abs">A Reputation for Excellence</h2>
<p class="intro abs">Our firm was founded in 1993 by Desmond T. Halvorsen, a member of the National Guild of Elder Care Counsel (NGECC) and an elder law practitioner for over 19 years.&nbsp; Our firm is uniquely positioned to provide quality legal advice and representation in regards to estate planning, wills, trusts, planning for people with disabilities...</p>
<div class="read-more abs"><i></i>Read More</div>

<section class="practice-left abs"></section>
<section class="practice-right abs"></section>
<svg class="practice-tab abs" viewBox="0 0 400 60" width="400" height="60"><path d="M0 60C30 60 30 4 70 4H330C370 4 370 60 400 60Z" fill="#fff"/></svg>
<h2 class="practice-heading abs">Our <span>Practice Areas</span></h2>

<!-- left column -->
<svg class="diamond abs" style="left:52px;top:1144px" viewBox="0 0 120 120"><rect x="24" y="24" width="72" height="72" transform="rotate(45 60 60)" fill="#fff" stroke="#1f4f86" stroke-width="3"/><circle cx="60" cy="60" r="18" fill="#3276b5"/></svg>
<div class="area on-blue abs" style="left:186px;top:1160px"><h3>Estate Planning</h3><p>Lorem ipsum dolor sit amet, consectetuer adipiscing elit,<br>sed diam nonummy nibh euismod tincidunt ut laoreet<br>dolore magna aliquam erat volutpat.</p></div>
<svg class="diamond abs" style="left:52px;top:1288px" viewBox="0 0 120 120"><rect x="24" y="24" width="72" height="72" transform="rotate(45 60 60)" fill="#fff" stroke="#1f4f86" stroke-width="3"/><circle cx="60" cy="60" r="18" fill="#3276b5"/></svg>
<div class="area on-blue abs" style="left:186px;top:1304px"><h3>Wills</h3><p>Lorem ipsum dolor sit amet, consectetuer adipiscing elit,<br>sed diam nonummy nibh euismod tincidunt ut laoreet<br>dolore magna aliquam erat volutpat.</p></div>
<svg class="diamond abs" style="left:52px;top:1432px" viewBox="0 0 120 120"><rect x="24" y="24" width="72" height="72" transform="rotate(45 60 60)" fill="#fff" stroke="#1f4f86" stroke-width="3"/><circle cx="60" cy="60" r="18" fill="#3276b5"/></svg>
<div class="area on-blue abs" style="left:186px;top:1448px"><h3>Trusts</h3><p>Lorem ipsum dolor sit amet, consectetuer adipiscing elit,<br>sed diam nonummy nibh euismod tincidunt ut laoreet<br>dolore magna aliquam erat volutpat.</p></div>
<svg class="diamond abs" style="left:52px;top:1576px" viewBox="0 0 120 120"><rect x="24" y="24" width="72" height="72" transform="rotate(45 60 60)" fill="#fff" stroke="#1f4f86" stroke-width="3"/><circle cx="60" cy="60" r="18" fill="#3276b5"/></svg>
<div class="area on-blue abs" style="left:186px;top:1592px"><h3>Planning For People With Disabilities</h3><p>Lorem ipsum dolor sit amet, consectetuer adipiscing elit,<br>sed diam nonummy nibh euismod tincidunt ut laoreet<br>dolore magna aliquam erat volutpat.</p></div>
<svg class="diamond abs" style="left:52px;top:1720px" viewBox="0 0 120 120"><rect x="24" y="24" width="72" height="72" transform="rotate(45 60 60)" fill="#fff" stroke="#1f4f86" stroke-width="3"/><circle cx="60" cy="60" r="18" fill="#3276b5"/></svg>
<div class="area on-blue abs" style="left:186px;top:1736px"><h3>Asset Protection And Preservation</h3><p>Lorem ipsum dolor sit amet, consectetuer adipiscing elit,<br>sed diam nonummy nibh euismod tincidunt ut laoreet<br>dolore magna aliquam erat volutpat.</p></div>
<svg class="diamond abs" style="left:52px;top:1864px" viewBox="0 0 120 120"><rect x="24" y="24" width="72" height="72" transform="rotate(45 60 60)" fill="#fff" stroke="#1f4f86" stroke-width="3"/><circle cx="60" cy="60" r="18" fill="#3276b5"/></svg>
<div class="area on-blue abs" style="left:186px;top:1880px"><h3>Medicaid Planning</h3><p>Lorem ipsum dolor sit amet, consectetuer adipiscing elit,<br>sed diam nonummy nibh euismod tincidunt ut laoreet<br>dolore magna aliquam erat volutpat.</p></div>
<svg class="diamond abs" style="left:52px;top:2008px" viewBox="0 0 120 120"><rect x="24" y="24" width="72" height="72" transform="rotate(45 60 60)" fill="#fff" stroke="#1f4f86" stroke-width="3"/><circle cx="60" cy="60" r="18" fill="#3276b5"/></svg>
<div class="area on-blue abs" style="left:186px;top:2024px"><h3>Hospital Safe Discharge</h3><p>Lorem ipsum dolor sit amet, consectetuer adipiscing elit,<br>sed diam nonummy nibh euismod tincidunt ut laoreet<br>dolore magna aliquam erat volutpat.</p></div>

<!-- right column -->
<svg class="diamond abs" style="left:630px;top:1144px" viewBox="0 0 120 120"><rect x="24" y="24" width="72" height="72" transform="rotate(45 60 60)" fill="#fff" stroke="#3276b5" stroke-width="3"/><circle cx="60" cy="60" r="18" fill="#3276b5"/></svg>
<div class="area on-black abs" style="left:762px;top:1160px"><h3>Nursing Home Placement</h3><p>Lorem ipsum dolor sit amet, consectetuer adipiscing elit,<br>sed diam nonummy nibh euismod tincidunt ut laoreet<br>dolore magna aliquam erat volutpat.</p></div>
<svg class="diamond abs" style="left:630px;top:1288px" viewBox="0 0 120 120"><rect x="24" y="24" width="72" height="72" transform="rotate(45 60 60)" fill="#fff" stroke="#3276b5" stroke-width="3"/><circle cx="60" cy="60" r="18" fill="#3276b5"/></svg>
<div class="area on-black abs" style="left:762px;top:1304px"><h3>Powers Of Attorney</h3><p>Lorem ipsum dolor sit amet, consectetuer adipiscing elit,<br>sed diam nonummy nibh euismod tincidunt ut laoreet<br>dolore magna aliquam erat volutpat.</p></div>
<svg class="diamond abs" style="left:630px;top:1432px" viewBox="0 0 120 120"><rect x="24" y="24" width="72" height="72" transform="rotate(45 60 60)" fill="#fff" stroke="#3276b5" stroke-width="3"/><circle cx="60" cy="60" r="18" fill="#3276b5"/></svg>
<div class="area on-black abs" style="left:762px;top:1448px"><h3>Health Care Proxies</h3><p>Lorem ipsum dolor sit amet, consectetuer adipiscing elit,<br>sed diam nonummy nibh euismod tincidunt ut laoreet<br>dolore magna aliquam erat volutpat.</p></div>
<svg class="diamond abs" style="left:630px;top:1576px" viewBox="0 0 120 120"><rect x="24" y="24" width="72" height="72" transform="rotate(45 60 60)" fill="#fff" stroke="#3276b5" stroke-width="3"/><circle cx="60" cy="60" r="18" fill="#3276b5"/></svg>
<div class="area on-black abs" style="left:762px;top:1592px"><h3>Living Wills</h3><p>Lorem ipsum dolor sit amet, consectetuer adipiscing elit,<br>sed diam nonummy nibh euismod tincidunt ut laoreet<br>dolore magna aliquam erat volutpat.</p></div>
<svg class="diamond abs" style="left:630px;top:1720px" viewBox="0 0 120 120"><rect x="24" y="24" width="72" height="72" transform="rotate(45 60 60)" fill="#fff" stroke="#3276b5" stroke-width="3"/><circle cx="60" cy="60" r="18" fill="#3276b5"/></svg>
<div class="area on-black abs" style="left:762px;top:1736px"><h3>Guardianships</h3><p>Lorem ipsum dolor sit amet, consectetuer adipiscing elit,<br>sed diam nonummy nibh euismod tincidunt ut laoreet<br>dolore magna aliquam erat volutpat.</p></div>
<svg class="diamond abs" style="left:630px;top:1864px" viewBox="0 0 120 120"><rect x="24" y="24" width="72" height="72" transform="rotate(45 60 60)" fill="#fff" stroke="#3276b5" stroke-width="3"/><circle cx="60" cy="60" r="18" fill="#3276b5"/></svg>
<div class="area on-black abs" style="left:762px;top:1880px"><h3>Probate</h3><p>Lorem ipsum dolor sit amet, consectetuer adipiscing elit,<br>sed diam nonummy nibh euismod tincidunt ut laoreet<br>dolore magna aliquam erat volutpat.</p></div>
<svg class="diamond abs" style="left:630px;top:2008px" viewBox="0 0 120 120"><rect x="24" y="24" width="72" height="72" transform="rotate(45 60 60)" fill="#fff" stroke="#3276b5" stroke-width="3"/><circle cx="60" cy="60" r="18" fill="#3276b5"/></svg>
<div class="area on-black abs" style="left:762px;top:2024px"><h3>Estate Administration &amp; Related Litigation</h3><p>Lorem ipsum dolor sit amet, consectetuer adipiscing elit,<br>sed diam nonummy nibh euismod tincidunt ut laoreet<br>dolore magna aliquam erat volutpat.</p></div>

<section class="tagline-band abs"></section>
<h2 class="tagline abs">We Care About Our Clients &amp; Believe In<br>Cultivating Long-term Relationships</h2>
<div class="accreditations abs"></div>
<div class="accred-label abs">Our<br>Accreditations</div>
<svg class="abs" style="left:290px;top:2380px" width="30" height="100" viewBox="0 0 30 100"><path d="M4 2 26 50 4 98" fill="none" stroke="rgba(255,255,255,.6)" stroke-width="3"/></svg>
<div class="partner abs" style="left:346px">Peak Counsel</div>
<div class="abs" style="left:598px;top:2414px;width:28px;height:28px;background:#fff"></div>
<div class="partner abs" style="left:636px;font-size:26px;top:2412px">Premier Barristers</div>
<div class="abs" style="left:862px;top:2380px;width:68px;height:96px;background:#fff;border-bottom:14px solid var(--brand-red)"></div>
<div class="abs" style="left:996px;top:2384px;width:90px;height:90px;border-radius:50%;background:#fff;border:6px solid var(--deep-blue)"></div>

<section class="call-band abs"></section>
<div class="call-text abs">CALL US TODAY</div>
<svg class="abs" style="left:576px;top:2557px" width="94" height="94" viewBox="0 0 94 94"><circle cx="47" cy="47" r="44" fill="none" stroke="rgba(255,255,255,.85)" stroke-width="3"/><circle cx="47" cy="47" r="36" fill="rgba(255,255,255,.15)"/></svg>
<div class="call-phone abs">(212) 555-0148</div>

<footer class="site-footer abs"></footer>
<div class="foot-title abs" style="left:78px">Quick Links</div>
<ul class="quick-links abs">
  <li>Home</li><li>Practice Areas</li><li>Privacy Policy</li><li>Attorneys</li><li>Contact &amp; Directions</li><li>News</li>
</ul>
<div class="foot-title abs" style="left:358px;width:200px">Contact Details</div>
<div class="contact-row abs" style="top:2748px">
  <svg width="14" height="18" viewBox="0 0 14 18"><path d="M7 0a7 7 0 0 0-7 7c0 5 7 11 7 11s7-6 7-11a7 7 0 0 0-7-7z" fill="#4aa0e6"/><circle cx="7" cy="7" r="2.5" fill="#2b2b2b"/></svg>
  <div><b>Manhattan:</b><br>318 Harlow Avenue, Suite 1204<br>New York, New York 10118</div>
</div>
<div class="contact-row abs" style="top:2816px">
  <svg width="14" height="14" viewBox="0 0 24 24"><path fill="#4aa0e6" d="M6.6 10.8a15 15 0 0 0 6.6 6.6l2.2-2.2c.3-.3.7-.4 1-.2 1.1.4 2.3.6 3.6.6.6 0 1 .4 1 1V20c0 .6-.4 1-1 1A17 17 0 0 1 3 4c0-.6.4-1 1-1h3.5c.6 0 1 .4 1 1 0 1.3.2 2.5.6 3.6.1.3 0 .7-.2 1z"/></svg>
  <div>(212) 555-0148</div>
</div>
<div class="contact-row abs" style="top:2848px">
  <svg width="16" height="14" viewBox="0 0 16 14"><rect x="3" y="0" width="10" height="5" fill="#4aa0e6"/><rect x="0" y="5" width="16" height="9" rx="2" fill="#4aa0e6"/></svg>
  <div>(212) 555-0172</div>
</div>
<div class="map-area abs" role="img" aria-label="Street map showing the office location in Midtown Manhattan"></div>

<div class="copyright-bar abs">Copyright ©&nbsp; 2016 Law Offices of Desmond T. Halvorsen, PLLC.&nbsp; All rights reserved</div>

</body>
</html>
```